One Page flat design for Car Classified Site

I'm looking for a flat design that that is very simple on the eye but with style. I need it to have a footer for some links etc, and the header needs a new feel but nothing to major.
This one page design is needed for the main page of the classified site...after this page is correct then all the other pages need to be designed to follow a similar style (new work).
I want more emphasis on the text rather than the images as a lot of users don't add images of the vehicles.
Attached is a mock up of the information and rough layout.
Wheelmarketlane.com is a classified site for car dealers only, I've also attached how the main competitions site looks.
Target Market(s)
Middle aged men, these guys are car dealers so it needs to be basic and easy for them as they aren't techie types.
Industry/Entity Type
Work
Number of Pages Required
1 page
Font styles to use
Look and feel

```html
<!DOCTYPE html>
<html lang="en">
<head>
<meta charset="utf-8">
<title>Wheelmarketlane.com – Car Listings</title>
<link href="https://fonts.googleapis.com/css2?family=Raleway:wght@400;500;600;700;800&display=swap" rel="stylesheet">
<style>
:root{
  --yellow:#fcc44f;
  --yellow-soft:#fde7b8;
  --cream:#fff7e6;
  --black:#000;
  --ink:#222;
  --muted:#555;
  --line:#e2e2e2;
  --footer:#3a3a3a;
  --pager:#3d3d3d;
  --white:#fff;
}
*{box-sizing:border-box;margin:0;padding:0}
html,body{width:902px;height:1200px;overflow:hidden}
body{font-family:"Raleway",sans-serif;color:var(--ink);background:var(--white);position:relative}

.site-header{height:75px;border-bottom:1px solid var(--line);background:linear-gradient(#fff 60%,#f4f4f4);position:relative}
.brand{position:absolute;left:104px;top:24px;font-size:22px;font-weight:800;letter-spacing:-.8px;color:var(--black)}
.main-nav{position:absolute;right:104px;top:30px;display:flex;gap:25px;align-items:center;font-size:11px;font-weight:500}
.main-nav svg{display:block}

.search{position:absolute;left:104px;top:94px;width:694px;height:200px}
.search-title{height:32px;background:var(--black);color:var(--white);font-size:14px;font-weight:500;padding:8px 22px}
.search-body{height:168px;background:var(--yellow);position:relative;border:1px solid #efb93f;border-top:none}
.select{position:absolute;width:159px;height:22px;background:var(--white);font-size:8.5px;color:var(--muted);padding:6px 9px}
.select.arrow::after{content:"";position:absolute;right:9px;top:8px;border:4px solid transparent;border-top:5px solid #666}
.btn{position:absolute;height:27px;font-size:11px;font-weight:600;display:flex;align-items:center;justify-content:center}
.btn-dark{background:var(--black);color:var(--white)}
.btn-soft{background:var(--yellow-soft);color:var(--black)}
.divider{position:absolute;left:364px;top:20px;width:1px;height:128px;background:#e2a93a}
.filter{position:absolute;top:24px}
.filter h3{font-size:11.5px;font-weight:500;color:var(--white);margin-bottom:4px}
.filter li{list-style:none;font-size:8.5px;height:16px;display:flex;align-items:center;gap:4px;color:#333}
.filter li::before{content:"";width:9px;height:9px;background:var(--white);display:block}

.listings{position:absolute;left:104px;top:305px;width:694px}
.listing-date{text-align:right;font-size:11px;color:var(--muted);height:21px}
.card{height:214px;border:1px solid var(--line);box-shadow:0 3px 4px rgba(0,0,0,.06);margin-bottom:14px;position:relative}
.card-head{height:32px;background:var(--yellow);display:flex;justify-content:space-between;align-items:center;padding:0 58px 0 17px}
.card-head h2{font-size:12px;font-weight:500;color:var(--black)}
.card-head p{font-size:10.5px;color:#333}
.photo{position:absolute;left:18px;top:50px;width:148px;height:90px;background:linear-gradient(160deg,#c9ccd0,#5b5e63 55%,#2a2b2e)}
.facts{position:absolute;top:50px;font-size:9px;line-height:16px;color:var(--muted)}
.facts b{font-weight:600;color:#333;display:block}
.offer{position:absolute;right:13px;top:49px;width:214px;height:126px;background:var(--cream);border:1px solid #fae8c4;text-align:center;padding-top:14px}
.offer h4{font-size:11px;font-weight:500;color:#f0b33a}
.offer small{font-size:6.8px;color:var(--muted);display:block;margin-top:3px}
.prices{display:flex;justify-content:space-around;margin-top:14px;font-size:9px;text-align:left}
.prices b{font-weight:600;display:block;color:#333;margin-bottom:4px}
.prices span{color:var(--muted)}
.card .btn{top:160px;height:27px;font-size:10px;font-weight:500}
.more{right:122px;width:105px}
.full{right:13px;width:104px;background:var(--yellow);color:var(--white)}
.specs{position:absolute;left:22px;top:162px;width:420px;font-size:7.5px;line-height:15px;color:var(--muted)}
.specs b{font-size:9.5px;font-weight:600;color:#333;display:block;margin-bottom:1px}

.pager{position:absolute;top:1072px;left:0;width:902px;display:flex;justify-content:center;gap:7px;padding-left:1px}
.pager span{height:17px;min-width:17px;padding:0 4px;background:var(--pager);color:var(--white);font-size:8px;font-weight:700;display:flex;align-items:center;justify-content:center;border-radius:1px}
.pager .wide{width:35px}

.site-footer{position:absolute;left:0;top:1125px;width:902px;height:75px;background:var(--footer);color:var(--white)}
.foot-nav{position:absolute;left:107px;top:21px;display:flex;gap:25px;font-size:10.5px;font-weight:500}
.copy{position:absolute;left:107px;top:45px;font-size:7.5px;color:#aaa}
.social{position:absolute;right:106px;top:24px;display:flex;gap:8px}
.social i{width:14px;height:14px;border-radius:50%;background:var(--white);display:block}
</style>
</head>
<body>

<header class="site-header">
  <div class="brand">WheelMarketLane</div>
  <nav class="main-nav">
    <svg width="16" height="14" viewBox="0 0 16 14" aria-label="Home"><path d="M8 0L0 7h2v7h4.5V9.5h3V14H14V7h2z" fill="#f5a623"/></svg>
    <span>Offered</span><span>Services</span><span>Deals</span><span>Wishlist</span><span>Account</span>
  </nav>
</header>

<section class="search">
  <div class="search-title">Search for a Car</div>
  <div class="search-body">
    <div class="select arrow" style="left:24px;top:19px">Make: Any</div>
    <div class="select arrow" style="left:190px;top:19px">Price: Any</div>
    <div class="select arrow" style="left:24px;top:46px">Body Type: Any</div>
    <div class="select arrow" style="left:190px;top:46px">Model: Any</div>
    <div class="select arrow" style="left:24px;top:75px">Age: Any</div>
    <div class="select" style="left:190px;top:75px">Enter keyword or listing Id</div>
    <div class="btn btn-dark" style="left:25px;top:108px;width:92px">Search Now</div>
    <div class="btn btn-soft" style="left:124px;top:108px;width:92px">Re-Submit</div>
    <div class="divider"></div>
    <div class="filter" style="left:397px"><h3>Body Style</h3><ul><li>Estate</li><li>Hathback</li><li>Saloon</li><li>Coupe</li><li>MP4</li><li>4WD</li></ul></div>
    <div class="filter" style="left:491px"><h3>Fuel</h3><ul><li>Petrol</li><li>Diesel</li><li>Hybrid</li><li>LPG</li><li>Electric</li><li>Automatic</li></ul></div>
    <div class="filter" style="left:589px"><h3>Car Status</h3><ul><li>Physical</li><li>Due in</li><li>Try in deal</li><li>Codisder swap</li></ul></div>
  </div>
</section>

<main class="listings">
  <div class="listing-date">Listing: Today</div>
  <article class="card">
    <div class="card-head"><h2>2013 Norvan Kestrel Sport DCI</h2><p>But it now for £13750 or please bid</p></div>
    <div class="photo" role="img" aria-label="Photo of dark grey coupe parked outside a building"></div>
    <div class="facts" style="left:183px"><b>History</b>2014 - 64<br>86000 Miles<br>Automatic<br>Black</div>
    <div class="facts" style="left:275px;top:66px">Northgate Motors<br>127 Miles Away<br>Etiam eu urna Sed porta Suspendi<br>Cum sociis natoque</div>
    <div class="offer"><h4>Try to deal my customer</h4><small>Cum sociis natoque penatibus et magnis dis parturi</small>
      <div class="prices"><div><b>Trade Price</b><span>£15,750</span></div><div><b>Retail Price</b><span>£17,750</span></div></div></div>
    <div class="specs"><b>Specs</b>Vivamus porttitor purus nisi eleifend libero a tempus libero lectus feugiat felis Morbi diam mauris viverra in gravida eu mattis in ante Morbi eget arcu Morbi porta libero</div>
    <div class="btn btn-dark more">More Information</div>
    <div class="btn full">Full Details</div>
  </article>

  <div class="listing-date">Listing: Today</div>
  <article class="card">
    <div class="card-head"><h2>2013 Norvan Kestrel Sport DCI</h2><p>But it now for £13750 or please bid</p></div>
    <div class="photo" role="img" aria-label="Photo of black saloon car on grass" style="background:linear-gradient(#5f8a3c,#3d5a2a 40%,#1e1f22 60%,#7f8a6c)"></div>
    <div class="facts" style="left:183px"><b>History</b>2014 - 64<br>86000 Miles<br>Automatic<br>Black</div>
    <div class="facts" style="left:275px;top:66px">Northgate Motors<br>127 Miles Away<br>Etiam eu urna Sed porta Suspendi<br>Cum sociis natoque</div>
    <div class="offer"><h4>Try to deal my customer</h4><small>Cum sociis natoque penatibus et magnis dis parturi</small>
      <div class="prices"><div><b>Trade Price</b><span>£15,750</span></div><div><b>Retail Price</b><span>£17,750</span></div></div></div>
    <div class="specs"><b>Specs</b>Vivamus porttitor purus nisi eleifend libero a tempus libero lectus feugiat felis Morbi diam mauris viverra in gravida eu mattis in ante Morbi eget arcu Morbi porta libero</div>
    <div class="btn btn-dark more">More Information</div>
    <div class="btn full">Full Details</div>
  </article>

  <div class="listing-date" style="margin-top:-13px">Listing: Today</div>
  <article class="card">
    <div class="card-head"><h2>2013 Norvan Kestrel Sport DCI</h2><p>But it now for £13750 or please bid</p></div>
    <div class="photo" role="img" aria-label="Studio photo of black saloon car" style="background:linear-gradient(150deg,#0d0d0f,#3c3f45 50%,#15161a)"></div>
    <div class="facts" style="left:183px"><b>History</b>2014 - 64<br>86000 Miles<br>Automatic<br>Black</div>
    <div class="facts" style="left:275px;top:66px">Northgate Motors<br>127 Miles Away<br>Etiam eu urna Sed porta Suspendi<br>Cum sociis natoque</div>
    <div class="offer"><h4>Try to deal my customer</h4><small>Cum sociis natoque penatibus et magnis dis parturi</small>
      <div class="prices"><div><b>Trade Price</b><span>£15,750</span></div><div><b>Retail Price</b><span>£17,750</span></div></div></div>
    <div class="specs"><b>Specs</b>Vivamus porttitor purus nisi eleifend libero a tempus libero lectus feugiat felis Morbi diam mauris viverra in gravida eu mattis in ante Morbi eget arcu Morbi porta libero</div>
    <div class="btn btn-dark more">More Information</div>
    <div class="btn full">Full Details</div>
  </article>
</main>

<nav class="pager">
  <span class="wide">Prev</span><span>1</span><span>2</span><span>3</span><span>4</span><span>5</span><span>6</span><span>…</span><span>22</span><span class="wide">Next</span>
</nav>

<footer class="site-footer">
  <nav class="foot-nav"><span>Home</span><span>Offered</span><span>Services</span><span>Deals</span><span>Wishlist</span><span>Account</span></nav>
  <p class="copy">© 2015 Company Name &nbsp;All right reserved &nbsp;Term of Use</p>
  <div class="social" aria-label="Social links"><i></i><i></i><i></i></div>
</footer>

</body>
</html>
```